Bright, Fun and hard to forget home inspection business card.

We need a Business card design for a new Home Inspection company. We are building a brand that is bright, fun and easy to remember.

Target Market(s)

Anyone involed in buying and selling of homes.

Industry/Entity Type

Home Inspection

Contact Information for Business Card

Colin Marlowe Owner/Inspector

Wedsite- PorchAndRafterCheck.example
Phone: 253-555-0187
Email- ColinMarlowe@mailbox.example
WA Lic # 4806

Requirements
Must have
• BRQV LOGO somewhere on card.

```html
<!DOCTYPE html>
<html lang="en">
<head>
<meta charset="utf-8">
<title>Porch And Rafter Check – Business Card</title>
<link href="https://fonts.googleapis.com/css2?family=Lato:wght@400;700;900&display=swap" rel="stylesheet">
<style>
  :root {
    --orange: #e2611f;
    --ink: #2a2a2a;
    --charcoal: #1f1f1f;
    --charcoal-light: #3a3a3a;
    --paper: #ffffff;
    --paper-shade: #ececec;
    --muted: #6b6b6b;
    --stage: #e6e4e0;
  }
  html, body {
    margin: 0;
    width: 1200px;
    height: 747px;
    overflow: hidden;
    background: var(--stage);
    font-family: "Lato", sans-serif;
  }
  .stage {
    position: relative;
    width: 1200px;
    height: 747px;
  }
  .card {
    position: absolute;
    top: 218px;
    width: 520px;
    height: 310px;
    border-radius: 3px;
    overflow: hidden;
    box-shadow: 0 6px 18px rgba(0,0,0,.18);
  }

  /* Front */
  .card--front {
    left: 50px;
    background: linear-gradient(135deg, var(--paper) 55%, var(--paper-shade));
  }
  .front__band-dark {
    position: absolute; top: 0; right: 26px; width: 14px; height: 100%;
    background: var(--charcoal);
  }
  .front__band-orange {
    position: absolute; top: 0; right: 0; width: 26px; height: 100%;
    background: var(--orange);
  }
  .front__brand {
    position: absolute; top: 34px; right: 74px;
    display: flex; align-items: center; gap: 12px;
  }
  .brand__dot {
    width: 34px; height: 34px; border-radius: 50%;
    background: var(--orange); flex: none;
  }
  .brand__name {
    font-weight: 900; font-size: 27px; line-height: 1.02;
    color: var(--ink); text-transform: uppercase; letter-spacing: .5px;
  }
  .front__badge {
    position: absolute; top: 150px; right: 74px;
    width: 46px; height: 46px; background: var(--charcoal);
  }
  .front__person {
    position: absolute; left: 40px; top: 128px;
  }
  .person__name {
    margin: 0; font-size: 20px; font-weight: 700; color: var(--orange);
  }
  .person__title {
    margin: 4px 0 0; font-size: 14px; color: var(--ink);
  }
  .front__contacts {
    position: absolute; left: 40px; bottom: 30px;
    list-style: none; margin: 0; padding: 0;
    font-size: 13px; color: var(--muted);
  }
  .contact {
    display: flex; align-items: center; gap: 8px; margin-top: 7px;
  }
  .contact__icon { width: 14px; height: 14px; flex: none; }

  /* Back */
  .card--back {
    left: 630px;
    background: linear-gradient(135deg, var(--charcoal-light), var(--charcoal) 60%);
  }
  .back__strip-white {
    position: absolute; top: 0; left: 0; width: 34px; height: 100%;
    background: var(--paper);
  }
  .back__strip-orange {
    position: absolute; top: 0; left: 34px; width: 12px; height: 100%;
    background: var(--orange);
  }
  .back__url {
    position: absolute; left: 17px; top: 50%;
    transform: translate(-50%, -50%) rotate(-90deg);
    white-space: nowrap; font-size: 10px; letter-spacing: 2.5px; color: var(--muted);
  }
  .back__brand {
    position: absolute; left: 46px; right: 0; top: 0; bottom: 0;
    display: flex; align-items: center; justify-content: center; gap: 16px;
  }
  .back__brand .brand__name {
    color: var(--paper); font-size: 34px;
  }
  .back__brand .brand__dot { width: 44px; height: 44px; }
</style>
</head>
<body>
<main class="stage">
  <section class="card card--front" aria-label="Business card front">
    <div class="front__brand">
      <span class="brand__dot"></span>
      <span class="brand__name">Porch And<br>Rafter Check<br>LLC</span>
    </div>
    <div class="front__badge" role="img" aria-label="Certification badge"></div>

    <div class="front__person">
      <p class="person__name">Colin Marlowe</p>
      <p class="person__title">Owner/Inspector</p>
    </div>

    <ul class="front__contacts">
      <li class="contact">
        <svg class="contact__icon" viewBox="0 0 14 14" aria-hidden="true"><circle cx="7" cy="7" r="7" fill="var(--orange)"/><path d="M4.5 4 l1.5 0 l.6 1.6 l-.9 .7 a5 5 0 0 0 2 2 l.7-.9 l1.6 .6 l0 1.5 a5.5 5.5 0 0 1-5.5-5.5z" fill="#fff"/></svg>
        253-555-0187
      </li>
      <li class="contact">
        <svg class="contact__icon" viewBox="0 0 14 14" aria-hidden="true"><circle cx="7" cy="7" r="7" fill="var(--orange)"/><rect x="3.5" y="4.5" width="7" height="5" fill="#fff"/><path d="M3.5 4.5 L7 7.3 L10.5 4.5" stroke="var(--orange)" stroke-width=".8" fill="none"/></svg>
        ColinMarlowe@mailbox.example
      </li>
      <li class="contact">
        <svg class="contact__icon" viewBox="0 0 14 14" aria-hidden="true"><circle cx="7" cy="7" r="7" fill="var(--orange)"/><circle cx="7" cy="7" r="3.6" fill="none" stroke="#fff" stroke-width="1"/><path d="M3.4 7 H10.6 M7 3.4 V10.6" stroke="#fff" stroke-width=".8"/></svg>
        PorchAndRafterCheck.example
      </li>
    </ul>

    <div class="front__band-dark"></div>
    <div class="front__band-orange"></div>
  </section>

  <section class="card card--back" aria-label="Business card back">
    <div class="back__strip-white"></div>
    <span class="back__url">www.PorchAndRafterCheck.example</span>
    <div class="back__strip-orange"></div>
    <div class="back__brand">
      <span class="brand__dot"></span>
      <span class="brand__name">Porch And<br>Rafter Check<br>LLC</span>
    </div>
  </section>
</main>
</body>
</html>
```